Sales Brochure

Industrial brochure of my industrial pump business which includes repair and sales of equipment. I distribute and repair industrial pumps for the midwest market. Design color is blue.

```html
<!DOCTYPE html>
<html lang="en">
<head>
<meta charset="utf-8">
<title>Prairie Flow Pump – Sales Brochure</title>
<link href="https://fonts.googleapis.com/css2?family=Inter:wght@300;400;500;600;700;800&display=swap" rel="stylesheet">
<style>
  :root {
    --brand-blue: #4f8fe6;
    --accent-blue: #78a9ee;
    --band-blue: #c0daff;
    --navy: #1f3a5f;
    --ink: #111418;
    --white: #ffffff;
    --label-blue: #8db8f5;
  }
  * { margin: 0; padding: 0; box-sizing: border-box; }
  html, body { width: 927px; height: 1200px; overflow: hidden; background: var(--white); }
  body { font-family: "Inter", Arial, sans-serif; color: var(--ink); position: relative; }

  .site-header { height: 109px; position: relative; }
  .brand { position: absolute; left: 55px; top: 26px; display: flex; align-items: center; gap: 10px; }
  .brand-dot { width: 58px; height: 58px; border-radius: 50%; background: var(--brand-blue); }
  .brand-text { display: flex; flex-direction: column; }
  .brand-name { font-size: 20px; font-weight: 800; color: var(--brand-blue); letter-spacing: 0.2px; }
  .brand-est { font-size: 13px; font-weight: 400; color: var(--accent-blue); margin-left: 62px; margin-top: 2px; }

  .hero { height: 404px; position: relative; overflow: hidden; }
  .hero-photo { position: absolute; inset: 0; background: linear-gradient(100deg, #4a4f55 0%, #3c4654 40%, #2f4d78 65%, #3a3f46 100%); }
  .hero-content { position: absolute; left: 55px; top: 98px; color: var(--white); }
  .hero-eyebrow { font-size: 20px; font-weight: 700; letter-spacing: 2.4px; }
  .hero-title { font-size: 44px; font-weight: 700; line-height: 50px; margin-top: 6px; letter-spacing: -0.3px; }
  .hero-sub { font-size: 24px; font-weight: 300; line-height: 29px; margin-top: 14px; width: 540px; }

  .about { height: 160px; background: var(--band-blue); text-align: center; padding-top: 23px; }
  .about h2 { font-size: 18px; font-weight: 700; }
  .about p { font-size: 13.4px; line-height: 19.8px; width: 660px; margin: 16px auto 0; }

  .content { position: relative; height: 432px; }
  .col { position: absolute; top: 27px; width: 400px; }
  .col-left { left: 55px; }
  .col-right { left: 476px; }
  .section-title { font-size: 18px; font-weight: 700; }
  .rule { width: 50px; height: 3px; background: var(--accent-blue); margin: 11px 0 15px; }
  .body-text { font-size: 12.3px; line-height: 17px; }
  .product-list { list-style: disc; margin: 10px 0 7px 45px; }
  .product-list li { font-size: 15px; font-weight: 600; line-height: 27px; }
  .expertise { margin-top: 38px; }
  .expertise-list { list-style: disc; margin: 8px 0 0 18px; }
  .expertise-list li { font-size: 12.3px; line-height: 16.6px; }
  .reasons p { font-size: 12.3px; line-height: 17px; margin-bottom: 7px; }
  .reasons strong { font-weight: 600; }
  .services { margin-top: 48px; }
  .service h3 { font-size: 15px; font-weight: 600; }
  .service p { margin: 3px 0 12px; font-size: 12.3px; }
  .service.large p { font-size: 13.4px; margin-bottom: 15px; }

  .contact { position: absolute; left: 0; top: 1105px; width: 927px; height: 95px; background: var(--navy); color: var(--white); }
  .contact h2 { position: absolute; left: 55px; top: 30px; font-size: 18px; font-weight: 700; }
  .label { font-size: 10.5px; font-weight: 600; color: var(--label-blue); letter-spacing: 0.8px; }
  .phone { position: absolute; left: 266px; top: 21px; }
  .phone-number { font-size: 20px; font-weight: 700; margin-top: 3px; }
  .office { position: absolute; left: 521px; top: 21px; font-size: 12.3px; line-height: 16px; }
  .office .label { line-height: 14px; }
  .office .email-label { margin-top: 2px; }
</style>
</head>
<body>
  <header class="site-header">
    <div class="brand">
      <span class="brand-dot"></span>
      <div class="brand-text">
        <span class="brand-name">PRAIRIE FLOW PUMP</span>
      </div>
    </div>
    <span class="brand-est" style="position:absolute;left:147px;top:74px;margin:0;">Est. 2021</span>
  </header>

  <section class="hero">
    <div class="hero-photo" role="img" aria-label="Row of blue industrial pumps with yellow couplings in a plant room"></div>
    <div class="hero-content">
      <div class="hero-eyebrow">PRAIRIE FLOW PUMP</div>
      <h1 class="hero-title">Your Midwest Industrial<br>Equipment Partner</h1>
      <p class="hero-sub">Delivering Reliable Pump Sales &amp; Repairs for Over 78 Years</p>
    </div>
  </section>

  <section class="about">
    <h2>ABOUT PRAIRIE FLOW PUMP</h2>
    <p>At Prairie Flow Pump, our vision is to become the leading provider of industrial equipment across the country. We are committed to delivering the highest quality products and services that empower our clients to succeed and grow. By staying at the forefront of industry trends and continuously improving our offerings, we aim to meet and exceed the needs of every customer.</p>
  </section>

  <main class="content">
    <div class="col col-left">
      <section class="products">
        <h2 class="section-title">OUR PRODUCTS</h2>
        <div class="rule"></div>
        <p class="body-text">We offer a comprehensive range of industrial equipment, including:</p>
        <ul class="product-list">
          <li>Pumps</li>
          <li>Motors</li>
          <li>Power Transmission Products</li>
        </ul>
        <p class="body-text">All of our products are sourced from trusted brands and are known for their reliability, durability, and efficiency.</p>
      </section>
      <section class="expertise">
        <h2 class="section-title">OUR EXPERTISE</h2>
        <div class="rule"></div>
        <p class="body-text">With over 78 years of combined experience in the industrial equipment industry, the Prairie Flow Pump team provides:</p>
        <ul class="expertise-list">
          <li>Expert advice to help you select the right equipment.</li>
          <li>Personalized service tailored to your business needs.</li>
          <li>Ongoing support to ensure your satisfaction long after the sale.</li>
        </ul>
      </section>
    </div>

    <div class="col col-right">
      <section class="reasons">
        <h2 class="section-title">WHY CHOOSE PRAIRIE FLOW PUMP?</h2>
        <div class="rule"></div>
        <p><strong>Experienced Technicians</strong> with in-depth knowledge of industrial systems.</p>
        <p><strong>High-Quality Equipment</strong> from industry-leading brands.</p>
        <p><strong>Quick Turnaround</strong> on repairs and service.</p>
      </section>
      <section class="services">
        <h2 class="section-title">OUR SERVICES</h2>
        <div class="rule"></div>
        <div class="service"><h3>Pump Sales</h3><p>Offering high-quality industrial pumps from top manufacturers.</p></div>
        <div class="service large"><h3>Pump Repairs</h3><p>Fast, reliable repairs to keep your operations running smoothly.</p></div>
        <div class="service large"><h3>Preventive Maintenance</h3><p>Extend equipment life and avoid costly breakdowns.</p></div>
      </section>
    </div>
  </main>

  <footer class="contact">
    <h2>CONTACT US</h2>
    <div class="phone">
      <div class="label">PHONE</div>
      <div class="phone-number">123 456 7890</div>
    </div>
    <div class="office">
      <div class="label">OFFICE LOCATION</div>
      <div>123 Industrial Lane, Midwest City, USA</div>
      <div class="label email-label">EMAIL</div>
      <div>info@prairieflowpump.com</div>
    </div>
  </footer>
</body>
</html>
```